Roofing & Siding door hanger flyer

-Looking to make door hanger flyer for Pellmont Roofing & Siding
-4.5" wide x 11" tall
-2 sided full colour
-We have started a new website (the content is changing) I have attached photos.
-About us:
-25 year labour warranty's available
-32 years in Calgary
-QCR A+ Member
-NWTG (Prairie Joint Shingle Guild) (logo attached)
-KOV Summit Select (logo attached)
-Owen Brisket (logo attached)
-Slogan "Raised On Care, Proven Through Seasons" 32 years in Calgary
-Sale
-Page 1 & 2 design ideas
We are in your area, contact us today for your Exclusive limited time offer! *discounts apply exclusively to new agreements only
Updates
-Please keep simple, clean & bright
-I really like the bright blue from our new logo (new logo uploaded)
-We specialize in Roofing -Siding-Gutters & full Exterior Renos (like the competitor example uploaded)
-This is the NEW website we are currently working on (not finished) https://mockview.example-draftpad.net/view/1a2b3c4d-5e6f-4a7b-8c9d-0e1f2a3b4c5d-7k2m/?fullscreen
-This is our OLD website https://pellmontshingleworks.com
-For the sale "We are in your area, contact us today for your Exclusive limited time offer" *discounts apply exclusively to new agreements only
-Free Estimates
-our phone# is 403-555-0148
-our website is pellmontshingleworks.com
-keep simple, clean, bright use the "new logo" uploaded. Check out the competitor example uploaded file
-We are in your area, Contact us today for your Exclusive limited time offer! *discounts apply to new agreements only
-FREE ESTIMATES
-Specialized in Roofing /Siding /Gutters Full Exterior Reno's
-We are currently working on a NEW website https://mockview.example-draftpad.net/view/1a2b3c4d-5e6f-4a7b-8c9d-0e1f2a3b4c5d-7k2m/?fullscreen
-Our OLD website https://pellmontshingleworks.com/
-Post old site address on flyer pellmontshingleworks.com
-Phone # 403-555-0148
Target Market(s)
40-55
Industry/Entity Type
Roofing Siding & full Exterior Reno's
Look and feel

```html
<!DOCTYPE html>
<html lang="en">
<head>
<meta charset="utf-8">
<title>Pellmont Door Hanger</title>
<link href="https://fonts.googleapis.com/css2?family=Montserrat:ital,wght@0,400;0,500;0,600;0,700;0,800;1,500;1,800&family=Oswald:wght@500;700&display=swap" rel="stylesheet">
<style>
:root{
  --stage:#cbcbcb;
  --paper:#ffffff;
  --brand-blue:#1f66b5;
  --bright-blue:#2a7fd4;
  --ink:#1e1e1e;
  --grey-text:#444444;
}
*{margin:0;padding:0;box-sizing:border-box}
html,body{width:1019px;height:1200px;overflow:hidden;background:var(--stage);font-family:"Montserrat",sans-serif}
.stage{position:relative;width:1019px;height:1200px}
.hanger{position:absolute;top:100px;width:409px;height:1000px;background:var(--paper);box-shadow:3px 5px 8px rgba(0,0,0,.25);overflow:hidden}
.hanger.front{left:78px}
.hanger.back{left:531px}
.abs{position:absolute}
.hang-cut{position:absolute;left:0;top:0;width:409px;height:200px}
.tagline{top:15px;left:0;width:100%;text-align:center;font-style:italic;font-weight:500;font-size:18.5px;color:var(--grey-text);letter-spacing:.3px}
.brand{top:292px;left:0;width:100%;text-align:center;color:var(--ink)}
.brand-name{font-weight:700;font-size:50px;letter-spacing:3px;line-height:50px;height:50px;display:inline-flex;align-items:center;gap:12px}
.brand-name .mark{width:22px;height:22px;background:var(--brand-blue)}
.brand-sub{font-weight:500;font-size:23px;line-height:26px;letter-spacing:5px;margin-top:12px;color:var(--ink);white-space:nowrap}
.photo{position:absolute;left:0;width:100%}
.tab{position:absolute;top:0;left:50%;transform:translateX(-50%);background:var(--paper);color:var(--brand-blue);font-weight:800;font-size:21px;text-align:center;height:30px;line-height:30px;border-radius:0 0 14px 14px;border-bottom:2px solid var(--brand-blue)}
.caption{color:#fff;font-size:14.5px;font-weight:500;white-space:nowrap;text-shadow:0 1px 2px rgba(0,0,0,.6)}
.bullets{list-style:none;color:#fff;font-size:13.2px;font-weight:500;line-height:15.5px;text-shadow:0 1px 2px rgba(0,0,0,.6);white-space:nowrap}
.bullets li::before{content:"";display:inline-block;width:5px;height:5px;border-radius:50%;background:var(--bright-blue);margin-right:6px;vertical-align:middle;box-shadow:0 0 0 1px #fff}
.url-pill{left:49px;width:312px;height:30px;border-radius:15px;background:var(--brand-blue);color:#fff;font-size:15.5px;text-align:center;line-height:26px;border:2px solid #fff;white-space:nowrap}
.url-pill b{font-weight:700}
.estimates{top:927px;left:0;width:100%;text-align:center;font-weight:600;font-size:24.5px;letter-spacing:1.5px;color:var(--grey-text)}
.phone{top:957px;left:0;width:100%;display:flex;justify-content:center;align-items:center;gap:8px;color:var(--brand-blue);font-weight:700;font-size:33px;letter-spacing:.5px}
.slogan-band{top:399px;left:0;width:100%;height:184px;background:linear-gradient(180deg,#2466b4 0%,#3a82cf 55%,#1f5fae 100%)}
.slogan{top:28px;left:0;width:100%;text-align:center;color:#fff;font-style:italic;font-weight:800;font-size:26.5px;line-height:34px;text-shadow:0 2px 3px rgba(0,0,0,.35)}
.years-box{top:119px;left:63px;width:277px;height:29px;border:2px solid #fff;color:#fff;text-align:center;line-height:25px;font-weight:600;font-size:17px;letter-spacing:.8px}
.about{top:604px;left:24px;width:252px;font-size:10.9px;line-height:13.7px;color:var(--ink)}
.warranty{top:598px;left:305px;width:82px;text-align:center;font-family:"Oswald",sans-serif;color:var(--brand-blue)}
.warranty .num{font-size:58px;font-weight:700;line-height:54px;display:inline-block;vertical-align:top}
.warranty .yrs{display:inline-block;writing-mode:vertical-rl;transform:rotate(180deg);font-size:18px;font-weight:700;line-height:18px;vertical-align:top;margin-top:2px}
.warranty .label{display:block;background:#555;color:#fff;font-size:8.6px;font-weight:500;padding:2px 0;margin-top:2px;border:1px solid #555}
.warranty .avail{display:block;color:#444;font-size:7px;margin-top:3px}
.offer{top:726px;left:0;width:100%;text-align:center;color:var(--bright-blue);font-weight:500;font-size:14.3px;line-height:18px}
.fineprint{top:769px;left:0;width:100%;text-align:center;font-size:11.8px;line-height:13px;color:var(--ink)}
.badges{top:813px;left:22px;width:365px;height:52px;display:flex;justify-content:space-between;align-items:center}
.badge{background:#d9dde4}
.rule{top:886px;height:2px;background:var(--brand-blue)}
.side-label{font-size:19px;color:#333;letter-spacing:1px;transform:rotate(-90deg);transform-origin:left top}
.concept{top:1137px;left:0;width:100%;text-align:center;font-size:19px;color:#222}
</style>
</head>
<body>
<div class="stage">

  <div class="hanger front">
    <div class="abs tagline">WE ARE IN YOUR NEIGHBOURHOOD</div>
    <svg class="hang-cut" viewBox="0 0 409 200" aria-hidden="true">
      <path fill="var(--stage)" d="M0,80 C60,96 110,112 150,104 L155,142 C110,138 60,150 0,166 Z"/>
      <path fill="var(--stage)" d="M409,80 C349,96 300,112 259,104 L254,142 C300,138 349,150 409,166 Z"/>
      <circle fill="var(--stage)" cx="206" cy="121" r="64"/>
    </svg>
    <div class="abs brand">
      <div class="brand-name"><span class="mark"></span>PELLMONT</div>
      <div class="brand-sub">ROOFING &amp; SIDING</div>
    </div>

    <div class="photo" style="top:395px;height:150px;background:linear-gradient(180deg,#7fa7d6 0%,#b8cde4 35%,#3b3e44 60%,#1d2024 100%)" role="img" aria-label="Photo of a house with a new dark asphalt shingle roof">
      <div class="tab" style="width:155px">ROOFING</div>
      <div class="abs caption" style="top:115px;left:0;width:100%;text-align:center">Asphalt • Rubber • Metal</div>
    </div>

    <div class="photo" style="top:545px;height:174px;background:linear-gradient(180deg,#4f86c9 0%,#a9c6e6 35%,#c99c76 60%,#5b4a3e 85%,#1f1f1f 100%)" role="img" aria-label="Photo of a house with fresh tan siding and a garage">
      <div class="tab" style="width:156px">SIDING</div>
      <ul class="abs bullets" style="top:125px;left:25px">
        <li>Brisket fibre cement</li>
        <li>Vinyl</li>
      </ul>
      <ul class="abs bullets" style="top:125px;left:210px">
        <li>Metal (Steel, Aluminum)</li>
        <li>Long Board</li>
      </ul>
    </div>

    <div class="photo" style="top:719px;height:172px;background:linear-gradient(180deg,#2e3a4f 0%,#556174 40%,#6b6656 65%,#1a1f29 100%)" role="img" aria-label="Photo of a home exterior at dusk with stone and siding">
      <div class="tab" style="width:225px">FULL EXTERIORS</div>
      <ul class="abs bullets" style="top:79px;left:25px">
        <li>Eavestrough/ Soffit/ Fascia</li>
        <li>Stone</li>
        <li>Skylights</li>
        <li>Windows &amp; Doors</li>
      </ul>
      <ul class="abs bullets" style="top:79px;left:281px">
        <li>Stucco</li>
        <li>Insulation</li>
        <li>Painting</li>
        <li>Shake Repairs</li>
      </ul>
    </div>

    <div class="abs url-pill" style="top:874px">www.<b>pellmontshingleworks</b>.com</div>
    <div class="abs estimates">FOR FREE ESTIMATES</div>
    <div class="abs phone">
      <svg width="34" height="34" viewBox="0 0 34 34" aria-hidden="true"><circle cx="17" cy="17" r="16" fill="var(--brand-blue)"/><path fill="#fff" d="M11.5 8.5c1-.6 2-.3 2.5.6l1.6 3c.4.8.2 1.6-.5 2.1l-1.2.9c.9 2 2.4 3.6 4.3 4.6l1-1.1c.6-.6 1.5-.7 2.2-.3l2.8 1.8c.9.6 1.1 1.6.5 2.5l-1 1.5c-.8 1.2-2.3 1.6-3.6 1.1-5-1.9-8.6-5.7-10.2-10.8-.4-1.3.1-2.8 1.3-3.6z"/></svg>
      <span>(403)-555-0148</span>
    </div>
  </div>

  <div class="hanger back">
    <div class="abs tagline">WE ARE IN YOUR NEIGHBOURHOOD</div>
    <svg class="hang-cut" viewBox="0 0 409 200" aria-hidden="true">
      <path fill="var(--stage)" d="M0,80 C60,96 110,112 150,104 L155,142 C110,138 60,150 0,166 Z"/>
      <path fill="var(--stage)" d="M409,80 C349,96 300,112 259,104 L254,142 C300,138 349,150 409,166 Z"/>
      <circle fill="var(--stage)" cx="206" cy="121" r="64"/>
    </svg>
    <div class="abs brand">
      <div class="brand-name"><span class="mark"></span>PELLMONT</div>
      <div class="brand-sub">ROOFING &amp; SIDING</div>
    </div>

    <div class="abs slogan-band" role="img" aria-label="Blue-tinted photo of a finished house front">
      <div class="abs slogan">Raised On Care<br>Proven Through Seasons</div>
      <div class="abs years-box">32 YEARS IN CALGARY</div>
    </div>

    <p class="abs about">We pride ourselves in providing excellent customer service and quality workmanship. We work with honesty and integrity and staff expert managers, supervisors and trades people. We provide satisfaction and ease of mind through our knowledge and experience throughout the duration of the project.</p>

    <div class="abs warranty">
      <span class="num">25</span><span class="yrs">YEARS</span>
      <span class="label">LABOUR WARRANTY'S</span>
      <span class="avail">AVAILABLE</span>
    </div>

    <div class="abs offer">We are in your area, contact us today<br>for your Exclusive limited time offer!</div>
    <div class="abs fineprint">*discounts apply exclusively to<br>new agreements only</div>

    <div class="abs badges">
      <div class="badge" style="width:44px;height:38px;border-radius:4px" role="img" aria-label="NWTG member badge"></div>
      <div class="badge" style="width:72px;height:28px;background:#1e4f8f;border-radius:3px" role="img" aria-label="QCR accredited business badge"></div>
      <div class="badge" style="width:32px;height:38px;background:#c8242b" role="img" aria-label="KOV materials badge"></div>
      <div class="badge" style="width:40px;height:40px;border-radius:50%;background:#c99a2e" role="img" aria-label="32 years anniversary seal"></div>
      <div class="badge" style="width:64px;height:30px;border-radius:4px" role="img" aria-label="Owen Brisket partner badge"></div>
      <div class="badge" style="width:40px;height:40px;background:#1e3f7a;transform:rotate(45deg)" role="img" aria-label="KOV Summit Select badge"></div>
    </div>

    <div class="abs rule" style="left:0;width:60px"></div>
    <div class="abs rule" style="left:349px;width:60px"></div>
    <div class="abs url-pill" style="top:873px">www.<b>pellmontshingleworks</b>.com</div>
    <div class="abs estimates">FOR FREE ESTIMATES</div>
    <div class="abs phone">
      <svg width="34" height="34" viewBox="0 0 34 34" aria-hidden="true"><circle cx="17" cy="17" r="16" fill="var(--brand-blue)"/><path fill="#fff" d="M11.5 8.5c1-.6 2-.3 2.5.6l1.6 3c.4.8.2 1.6-.5 2.1l-1.2.9c.9 2 2.4 3.6 4.3 4.6l1-1.1c.6-.6 1.5-.7 2.2-.3l2.8 1.8c.9.6 1.1 1.6.5 2.5l-1 1.5c-.8 1.2-2.3 1.6-3.6 1.1-5-1.9-8.6-5.7-10.2-10.8-.4-1.3.1-2.8 1.3-3.6z"/></svg>
      <span>(403)-555-0148</span>
    </div>
  </div>

  <div class="abs side-label" style="left:42px;top:1100px">FRONT</div>
  <div class="abs side-label" style="left:955px;top:1098px">BACK</div>
  <div class="abs concept">Design Concept Pellmont Door Hanger 01</div>
</div>
</body>
</html>
```